Design Labels for branding of products

We need labels designed for a few things
1- A Coffee Coconut Body Scrub,
This a body scrub that gives a great exfoliation and moisturisation
our competiition is Mellowskin and Drpeachglow
2 - An anti Wrinkle Night Oil
This is a night oil that is applied at night and helps with wrinkles, scars, cellulite, age spots, strecth marks
3 - Sun Tan Lotion
This is a natural organic lotion that when applied before going in the sun with help with increasing your natural brown and give a slight spf, it is great for tanning and for skin hydration.
4 - Fake tan Spray
This is simply a spray bottle that is sprayed over the body to give a fake tan for several days.
Need all designs to relate to each other as we are trying to create a brand
We have a website with our logo on it
www.wavelumescrubs.com.au

```html
<!DOCTYPE html>
<html lang="en">
<head>
<meta charset="utf-8">
<title>Wavelumescrubs – Product Label Range</title>
<link rel="stylesheet" href="https://fonts.googleapis.com/css2?family=Great+Vibes&family=Rajdhani:wght@400;500&family=Montserrat:wght@600&display=swap">
<style>
  :root {
    --backdrop-top: #f4f4f5;
    --backdrop-bottom: #d9dadc;
    --label-white: #f7f8f8;
    --label-edge: #e2e4e6;
    --brand-blue: #2b8cc2;
    --ring-blue: #7cb8da;
    --ring-soft: #dfe6ea;
    --body-grey: #5d6165;
    --tagline-grey: #6a6e72;
  }
  * { box-sizing: border-box; margin: 0; padding: 0; }
  html, body { width: 1200px; height: 675px; overflow: hidden; }
  body {
    background: linear-gradient(180deg, var(--backdrop-top) 0%, var(--backdrop-bottom) 100%);
    font-family: "Rajdhani", sans-serif;
  }
  .label-range {
    width: 1200px; height: 675px;
    display: flex; align-items: flex-end; justify-content: center;
    gap: 34px; padding: 0 40px 70px;
  }
  .label {
    background: var(--label-white);
    border: 1px solid var(--label-edge);
    border-radius: 4px;
    box-shadow: 0 6px 18px rgba(0,0,0,0.08);
    display: flex; flex-direction: column; align-items: center;
    text-align: center;
  }
  .brand { margin-top: 28px; display: flex; flex-direction: column; align-items: center; }
  .brand-name {
    font-family: "Montserrat", sans-serif; font-weight: 600;
    color: var(--brand-blue); letter-spacing: 0.02em; line-height: 1;
  }
  .brand-tagline {
    font-family: "Montserrat", sans-serif; font-weight: 600;
    color: var(--tagline-grey); letter-spacing: 0.03em; margin-top: 3px;
  }
  .brand-emblem { display: block; margin-top: 16px; }
  .product-name {
    font-family: "Great Vibes", cursive;
    color: var(--brand-blue); line-height: 1; font-weight: 400;
  }
  .product-variant { color: var(--body-grey); font-weight: 500; line-height: 1; }
  .product-copy { color: var(--body-grey); text-align: justify; line-height: 1.25; }

  /* Sun Tan Lotion */
  .label--lotion { width: 240px; height: 380px; }
  .label--lotion .brand-name { font-size: 15px; }
  .label--lotion .brand-tagline { font-size: 6.5px; }
  .label--lotion .product-name { font-size: 40px; margin-top: 18px; }
  .label--lotion .product-copy { font-size: 11.5px; width: 196px; margin-top: 10px; }

  /* Tan Spray */
  .label--spray { width: 200px; height: 300px; }
  .label--spray .brand { margin-top: 24px; }
  .label--spray .brand-name { font-size: 13px; }
  .label--spray .brand-tagline { font-size: 5.6px; }
  .label--spray .brand-emblem { margin-top: 12px; }
  .label--spray .product-name { font-size: 42px; margin-top: 10px; }
  .label--spray .product-copy { font-size: 11.5px; width: 166px; margin-top: 10px; text-align: center; }

  /* Night Oil */
  .label--oil { width: 150px; height: 230px; }
  .label--oil .brand { margin-top: 20px; }
  .label--oil .brand-name { font-size: 10px; }
  .label--oil .brand-tagline { font-size: 4.4px; }
  .label--oil .brand-emblem { margin-top: 10px; }
  .label--oil .product-name { font-size: 32px; margin-top: 8px; }
  .label--oil .product-variant { font-size: 12px; margin-top: 2px; align-self: flex-end; margin-right: 18px; }
  .label--oil .product-copy { font-size: 9.5px; width: 124px; margin-top: 8px; text-align: center; }

  /* Body Scrub pouch */
  .label--scrub { width: 320px; height: 470px; }
  .label--scrub .brand { margin-top: 40px; }
  .label--scrub .brand-name { font-size: 16px; }
  .label--scrub .brand-tagline { font-size: 7px; }
  .label--scrub .brand-emblem { margin-top: 26px; }
  .label--scrub .product-name { font-size: 56px; margin-top: 24px; align-self: flex-end; margin-right: 26px; }
  .label--scrub .product-variant { font-size: 22px; align-self: flex-end; margin-right: 26px; margin-top: -2px; }
  .label--scrub .product-copy { font-size: 14px; width: 270px; margin-top: 10px; }
</style>
</head>
<body>
<main class="label-range">

  <section class="label label--lotion">
    <div class="brand">
      <span class="brand-name">WAVELUMESCRUBS</span>
      <span class="brand-tagline">COFFEE COCONUT BODY SCRUB</span>
    </div>
    <svg class="brand-emblem" width="100" height="100" viewBox="0 0 100 100" aria-hidden="true">
      <circle cx="50" cy="50" r="48" fill="none" stroke="var(--ring-soft)" stroke-width="2"/>
      <circle cx="50" cy="50" r="36" fill="none" stroke="var(--ring-blue)" stroke-width="1.6"/>
    </svg>
    <h2 class="product-name">Sun Tan Lotion</h2>
    <p class="product-copy">This is a natural organic lotion that when applied before going in the sun with help with increasing your natural brown and give a slight spf, it is great for tanning and for skin hydration.</p>
  </section>

  <section class="label label--spray">
    <div class="brand">
      <span class="brand-name">WAVELUMESCRUBS</span>
      <span class="brand-tagline">COFFEE COCONUT BODY SCRUB</span>
    </div>
    <svg class="brand-emblem" width="82" height="82" viewBox="0 0 100 100" aria-hidden="true">
      <circle cx="50" cy="50" r="48" fill="none" stroke="var(--ring-soft)" stroke-width="2"/>
      <circle cx="50" cy="50" r="36" fill="none" stroke="var(--ring-blue)" stroke-width="1.8"/>
    </svg>
    <h2 class="product-name">Tan Spray</h2>
    <p class="product-copy">simply spray over your body to give a fake tan for several days</p>
  </section>

  <section class="label label--oil">
    <div class="brand">
      <span class="brand-name">WAVELUMESCRUBS</span>
      <span class="brand-tagline">COFFEE COCONUT BODY SCRUB</span>
    </div>
    <svg class="brand-emblem" width="60" height="60" viewBox="0 0 100 100" aria-hidden="true">
      <circle cx="50" cy="50" r="48" fill="none" stroke="var(--ring-soft)" stroke-width="2.4"/>
      <circle cx="50" cy="50" r="36" fill="none" stroke="var(--ring-blue)" stroke-width="2.2"/>
    </svg>
    <h2 class="product-name">Night Oil</h2>
    <span class="product-variant">Anti Wrinkle</span>
    <p class="product-copy">helps with wrinkles, scars, cellulite, age spots, strecth marks</p>
  </section>

  <section class="label label--scrub">
    <div class="brand">
      <span class="brand-name">WAVELUMESCRUBS</span>
      <span class="brand-tagline">COFFEE COCONUT BODY SCRUB</span>
    </div>
    <svg class="brand-emblem" width="110" height="110" viewBox="0 0 100 100" aria-hidden="true">
      <circle cx="50" cy="50" r="48" fill="none" stroke="var(--ring-soft)" stroke-width="2"/>
      <circle cx="50" cy="50" r="36" fill="none" stroke="var(--ring-blue)" stroke-width="1.6"/>
    </svg>
    <h2 class="product-name">Body Scrub</h2>
    <span class="product-variant">Coffee Coconut</span>
    <p class="product-copy">This a body scrub that gives a great exfoliation and moisturisation our competition is Mellowskin and Drpeachglow</p>
  </section>

</main>
</body>
</html>
```